Business Card Design

We need a business card design for an existing business. Our main trading brand is www.brightquillsaver.co.uk

We attach various logo files - please use the version that will produce the sharpest image on the business card.

We are flexible about shape of card etc. Please think outside the box as to what goes on front and what goes on back of the card

We want to be able to amend the card (once the design has been agreed ) to add additional staff details, but the text to go on it will be generic

Details to go on card ( for the first generic one) are fairly minimal as we don't like cluttered business cards:-

Neil Cathcart
Managing Director

Mobile: 07841 258 407
Email: n.cathcart@brightquillsaver.co.uk

Industry/Entity Type

Business

```html
<!DOCTYPE html>
<html lang="en">
<head>
<meta charset="utf-8">
<title>Brightquillsaver business card</title>
<link rel="stylesheet" href="https://fonts.googleapis.com/css2?family=Questrial&family=Michroma&display=swap">
<style>
  :root {
    --backdrop: #d9dcdf;
    --card-white: #ffffff;
    --card-mist: #e6e8ea;
    --navy: #355a78;
    --sky: #4aa8e0;
    --sky-soft: #8cc6ea;
    --ink-light: #ffffff;
  }
  html, body {
    margin: 0;
    padding: 0;
    width: 1200px;
    height: 900px;
    overflow: hidden;
    background: var(--backdrop);
  }
  .canvas {
    position: relative;
    width: 1200px;
    height: 900px;
  }
  .card {
    position: absolute;
    left: 240px;
    width: 720px;
    height: 410px;
    border-radius: 38px;
    overflow: hidden;
    box-shadow: 0 10px 28px rgba(40, 50, 60, 0.22);
    background: radial-gradient(ellipse at 60% 30%, var(--card-white) 0%, var(--card-mist) 100%);
  }
  .card--front { top: 30px; }
  .card--back { top: 460px; }
  .card svg { display: block; width: 100%; height: 100%; }
  .wordmark {
    font-family: "Questrial", sans-serif;
    font-size: 34px;
    fill: var(--sky);
  }
  .person-name {
    font-family: "Michroma", sans-serif;
    font-size: 17px;
    letter-spacing: 2px;
    fill: var(--sky);
  }
  .person-role {
    font-family: "Michroma", sans-serif;
    font-size: 13px;
    letter-spacing: 2px;
    fill: var(--sky);
  }
  .contact-line {
    font-family: "Michroma", sans-serif;
    font-size: 10px;
    letter-spacing: 0.4px;
    fill: var(--ink-light);
  }
  .contact-icon circle { fill: var(--ink-light); }
  .contact-icon path, .contact-icon rect { fill: none; stroke: var(--navy); stroke-width: 1.3; }
  .brand-dot { fill: var(--sky-soft); }
</style>
</head>
<body>
<main class="canvas">

  <section class="card card--front" aria-label="Card front">
    <svg viewBox="0 0 720 410" xmlns="http://www.w3.org/2000/svg">
      <path class="navy-panel" d="M0,205 C190,300 470,300 720,150 L720,410 L0,410 Z" fill="var(--navy)"/>
      <path class="sky-swoosh" d="M0,180 C190,280 470,282 720,124" fill="none" stroke="var(--sky)" stroke-width="7"/>

      <text class="wordmark" x="118" y="92">brightquillsaver.co.uk</text>
      <circle class="brand-dot" cx="578" cy="80" r="20"/>

      <text class="person-name" x="44" y="150">NEIL CATHCART</text>
      <text class="person-role" x="44" y="176">OWNER / C.E.O</text>

      <g class="contact-list">
        <g class="contact-icon" transform="translate(350,300)">
          <circle r="7"/><path d="M-3.5,3 V-0.5 L0,-3.5 L3.5,-0.5 V3 Z"/>
        </g>
        <text class="contact-line" x="364" y="304">SUITE # 410, KELL BLDG,</text>
        <text class="contact-line" x="364" y="319">NY 74218</text>

        <g class="contact-icon" transform="translate(350,330)">
          <circle r="7"/><path d="M-3,-3.5 L-1,-3.5 L0,-1 L-1.2,0 Q-0.3,1.8 1.2,2.4 L2,1.2 L3.6,2.2 L3.2,3.6 Q-3.6,3 -3,-3.5 Z"/>
        </g>
        <text class="contact-line" x="364" y="334">07841 258 407</text>

        <g class="contact-icon" transform="translate(350,346)">
          <circle r="7"/><rect x="-2.3" y="-4" width="4.6" height="8" rx="1"/>
        </g>
        <text class="contact-line" x="364" y="350">07852 614 930</text>

        <g class="contact-icon" transform="translate(350,362)">
          <circle r="7"/><rect x="-3.8" y="-2" width="7.6" height="4.6" rx="0.6"/><path d="M-3.8,-2 V-3.6 H3.8 V-2"/>
        </g>
        <text class="contact-line" x="364" y="366">01632 960 472</text>

        <g class="contact-icon" transform="translate(350,378)">
          <circle r="7"/><rect x="-4" y="-2.8" width="8" height="5.6"/><path d="M-4,-2.8 L0,0.6 L4,-2.8"/>
        </g>
        <text class="contact-line" x="364" y="382">N.CATHCART@BRIGHTQUILLSAVER.CO.UK</text>

        <g class="contact-icon" transform="translate(350,394)">
          <circle r="7"/><path d="M-4,0 H4 M0,-4 V4 M0,-4 Q-3,0 0,4 Q3,0 0,-4"/>
        </g>
        <text class="contact-line" x="364" y="398">WWW.BRIGHTQUILLSAVER.CO.UK</text>
      </g>
    </svg>
  </section>

  <section class="card card--back" aria-label="Card back">
    <svg viewBox="0 0 720 410" xmlns="http://www.w3.org/2000/svg">
      <text class="wordmark" x="340" y="216" text-anchor="middle">brightquillsaver.co.uk</text>
      <circle class="brand-dot" cx="590" cy="204" r="22"/>
    </svg>
  </section>

</main>
</body>
</html>
```